Consultants Need a Powerful New Image to Support a New Concept

We need a better image for an idea we have. Will be used in powerpoint but also in print (workbooks, handouts etc). The notion is that in any moment people in an organisation can choose to tell positive stories about what is going well, what they enjoy, what they are hopeful for or negative stories about what is wrong, not working or they are frustrated and pissed off about.

Target Market(s)

Leaders in organisations

Industry/Entity Type

It Support

Font styles to use
Sans Serif

Requirements
Must have
• The ability to build the image in powerpoint (at least add the text). Needs also to be used as a stand alone. Font and palette consistency with other materials. Some examples attached as well as font files and colour guidelines. Notice the left hand side of the model is about tell the stories and the right hand side is about how telling positive stories encourages others to seek more positive stories. On the right hand side down the bottom, the point is that these negative stories are so easy to join in on and they spread quickly and breed cynicism. Note the "Storyline" running up and down the middle - storyline model attached.
Nice to have
• A sense of momentum both up and down - the more positive stories we tell the more the organisation is energised and positive, the more negative stories (whingeing and complaining) the worse it is.

```html
<!DOCTYPE html>
<html lang="en">
<head>
<meta charset="utf-8">
<title>The Conversational Moment</title>
<link href="https://fonts.googleapis.com/css2?family=Montserrat:wght@500;700;800&display=swap" rel="stylesheet">
<style>
  :root {
    --green: #a2c11c;
    --blue: #0c62ae;
    --ink: #1d1d1b;
    --navy: #3b3d6b;
    --dots: #c9c9c9;
    --white: #ffffff;
  }
  html, body {
    margin: 0;
    padding: 0;
    width: 1200px;
    height: 690px;
    overflow: hidden;
    background: var(--white);
  }
  .model {
    display: block;
    width: 1200px;
    height: 690px;
    font-family: "Montserrat", Arial, sans-serif;
  }
  .panel--positive { fill: var(--green); }
  .panel--negative { fill: var(--blue); }
  .moment-circle { fill: var(--white); }
  .moment-mark { fill: var(--ink); font-size: 48px; font-weight: 800; }
  .moment-label { fill: var(--ink); font-size: 9.5px; font-weight: 800; }
  .head-text { fill: var(--white); font-size: 17px; font-weight: 700; }
  .tell--positive { fill: var(--green); font-size: 18px; font-weight: 800; }
  .tell--negative { fill: var(--blue); font-size: 18px; font-weight: 800; }
  .storyline { fill: none; stroke: var(--dots); stroke-width: 3; stroke-linecap: round; stroke-dasharray: 0.1 7; }
  .dot--positive { fill: var(--green); }
  .dot--negative { fill: var(--blue); }
  .step-label { fill: var(--ink); font-size: 16px; font-weight: 500; }
  .stage--positive { fill: var(--green); font-size: 25px; font-weight: 800; }
  .stage--negative { fill: var(--blue); font-size: 25px; font-weight: 800; }
  .brand-name { fill: var(--navy); font-size: 32px; font-weight: 500; }
  .brand-dot { fill: var(--navy); }
</style>
</head>
<body>
<svg class="model" viewBox="0 0 1200 690" xmlns="http://www.w3.org/2000/svg">

  <!-- Story panels -->
  <rect class="panel--positive" role="img" aria-label="Green profile figure facing left: the positive storyteller"
        x="372" y="144" width="222" height="304" rx="60"/>
  <rect class="panel--positive" x="500" y="144" width="94" height="304"/>
  <rect class="panel--negative" role="img" aria-label="Blue profile figure facing right: the negative storyteller"
        x="606" y="144" width="222" height="304" rx="60"/>
  <rect class="panel--negative" x="606" y="144" width="94" height="304"/>

  <!-- The conversational moment -->
  <circle class="moment-circle" cx="600" cy="262" r="66"/>
  <text class="moment-mark" x="600" y="242" text-anchor="middle">?</text>
  <text class="moment-label" x="600" y="270" text-anchor="middle">THE</text>
  <text class="moment-label" x="600" y="283" text-anchor="middle">CONVERSATIONAL</text>
  <text class="moment-label" x="600" y="296" text-anchor="middle">MOMENT</text>

  <!-- Panel statements -->
  <text class="head-text" text-anchor="end">
    <tspan x="524" y="272">SEEK</tspan>
    <tspan x="524" y="294">STORIES:</tspan>
    <tspan x="524" y="316">Catch People</tspan>
    <tspan x="524" y="338">Doing Things</tspan>
    <tspan x="524" y="360">Right</tspan>
  </text>
  <text class="head-text">
    <tspan x="678" y="272">JOIN</tspan>
    <tspan x="678" y="294">STORIES:</tspan>
    <tspan x="678" y="316">Cynicism,</tspan>
    <tspan x="678" y="338">Sarcasm &amp;</tspan>
    <tspan x="678" y="360">Negativity</tspan>
  </text>

  <!-- Tell stories -->
  <text class="tell--positive" text-anchor="end">
    <tspan x="588" y="478">TELL STORIES:</tspan>
    <tspan x="588" y="503">Bright Spots &amp;</tspan>
    <tspan x="588" y="528">Possibility</tspan>
  </text>
  <text class="tell--negative">
    <tspan x="612" y="478">TELL STORIES:</tspan>
    <tspan x="612" y="503">Complaint &amp;</tspan>
    <tspan x="612" y="528">Failure</tspan>
  </text>

  <!-- Positive storyline -->
  <path class="storyline" d="M356,158 C344,196 326,226 323,250 C318,285 316,312 316,340 C318,372 324,400 328,430 C334,462 346,492 362,520"/>
  <circle class="dot--positive" cx="356" cy="158" r="11"/>
  <circle class="dot--positive" cx="323" cy="250" r="11"/>
  <circle class="dot--positive" cx="316" cy="340" r="11"/>
  <circle class="dot--positive" cx="328" cy="430" r="11"/>
  <circle class="dot--positive" cx="362" cy="520" r="11"/>

  <text class="step-label" text-anchor="end"><tspan x="332" y="153">Changes</tspan><tspan x="332" y="174">Awareness</tspan></text>
  <text class="step-label" text-anchor="end"><tspan x="300" y="243">Gives Insight,</tspan><tspan x="300" y="264">Shapes Beliefs</tspan></text>
  <text class="step-label" text-anchor="end"><tspan x="290" y="334">Builds</tspan><tspan x="290" y="355">Confidence</tspan></text>
  <text class="step-label" text-anchor="end"><tspan x="303" y="425">Encourages</tspan><tspan x="303" y="446">Proactive Behaviour</tspan></text>
  <text class="step-label" text-anchor="end"><tspan x="337" y="515">Supports</tspan><tspan x="337" y="536">Performance</tspan></text>

  <text class="stage--positive" x="336" y="213" text-anchor="middle">SEE</text>
  <text class="stage--positive" x="317" y="304" text-anchor="middle">BE</text>
  <text class="stage--positive" x="320" y="392" text-anchor="middle">DO</text>
  <text class="stage--positive" x="340" y="481" text-anchor="middle">GET</text>

  <!-- Negative storyline -->
  <path class="storyline" d="M844,155 C858,196 872,224 875,250 C880,285 886,312 886,340 C884,372 876,402 872,432 C866,464 852,494 838,521"/>
  <circle class="dot--negative" cx="844" cy="155" r="11"/>
  <circle class="dot--negative" cx="875" cy="250" r="11"/>
  <circle class="dot--negative" cx="886" cy="340" r="11"/>
  <circle class="dot--negative" cx="872" cy="432" r="11"/>
  <circle class="dot--negative" cx="838" cy="521" r="11"/>

  <text class="step-label"><tspan x="866" y="153">Fuels Unhelpful</tspan><tspan x="866" y="174">Beliefs</tspan></text>
  <text class="step-label"><tspan x="897" y="240">Builds Negative</tspan><tspan x="897" y="261">energy</tspan></text>
  <text class="step-label"><tspan x="906" y="333">Destroys</tspan><tspan x="906" y="354">Confidence</tspan></text>
  <text class="step-label"><tspan x="893" y="423">Discourages</tspan><tspan x="893" y="444">Effort and Action</tspan></text>
  <text class="step-label"><tspan x="858" y="515">Undermines</tspan><tspan x="858" y="536">Performance</tspan></text>

  <text class="stage--negative" x="864" y="213" text-anchor="middle">SEE</text>
  <text class="stage--negative" x="882" y="304" text-anchor="middle">BE</text>
  <text class="stage--negative" x="884" y="392" text-anchor="middle">DO</text>
  <text class="stage--negative" x="860" y="481" text-anchor="middle">GET</text>

  <!-- Brand -->
  <circle class="brand-dot" cx="96" cy="622" r="16"/>
  <text class="brand-name" x="122" y="634">Kestrel</text>
</svg>
</body>
</html>
```